LV Business Card NEEDED

Larch Vantage is a finance brokering company that provide lending advise to consumer, business, corporate, and property developer for all their financing needs.

We source and match customer needs in Home Loan, Business Loan, Commercial Property Loan, Assets Finance, and other banking related services. It is a market with full of loans! But we specialise in more complex loan structure and our client base are more business and corporate level. Our suppliers are Banks and large Financial Institution where these business card will go to.

We have a great deal of Asian clients, therefore the card need to also include Chinese language together with English.

Refer to attached file for logo and content requirements.

We are looking for designs with the following ingredients:
* Innovative & Creative
* Professional
* Trust & Security

Please pick colours that will compliment the colours of the company logo.

Please provide a unique design, for example the edge of the card is rounded or corner cut off.

Company logo uploaded.

Please commence submitting your design.

Target Market(s)

Target audiences are businessmen, corporate, and property developer. And also a great deal of Chinese clients.

Industry/Entity Type

Finance

Contact Information for Business Card

Larch Vantage Pty. Ltd.
Morris Pelham
Director
Suite 27, 3-9 Quenby St. Auburn NSW 2144

Requirements
Must have
• Double sided design

```html
<!DOCTYPE html>
<html lang="en">
<head>
<meta charset="utf-8">
<title>Larch Vantage – Business Card</title>
<link rel="stylesheet" href="https://fonts.googleapis.com/css2?family=Roboto:wght@300;400&family=Cormorant+Garamond:wght@400&family=Noto+Sans+TC:wght@400&family=Noto+Serif+TC:wght@400&display=swap">
<style>
  :root {
    --bg: #e9eaec;
    --navy-deep: #0d1c35;
    --navy: #1d3a66;
    --navy-light: #2c5288;
    --silver: #c9ccd1;
    --paper: #ffffff;
    --paper-shade: #eceef1;
    --ink: #1a1a1a;
    --label: #8a8d92;
    --gold: #c9a23a;
    --back-text: #c7d0de;
  }
  * { margin: 0; padding: 0; box-sizing: border-box; }
  html, body { width: 1200px; height: 901px; overflow: hidden; }
  body {
    background: var(--bg);
    position: relative;
    font-family: "Roboto", Arial, sans-serif;
  }
  .card {
    position: absolute;
    top: 288px;
    width: 540px;
    height: 324px;
    border-radius: 22px;
    overflow: hidden;
    box-shadow: 0 6px 20px rgba(0,0,0,.18);
  }

  /* ---------- Back side ---------- */
  .card-back {
    left: 40px;
    background: radial-gradient(ellipse at 50% 30%, var(--navy-light) 0%, var(--navy) 45%, var(--navy-deep) 100%);
    color: var(--back-text);
    text-align: center;
  }
  .back-mark {
    position: absolute;
    left: 50%; top: 58px;
    transform: translateX(-50%);
    width: 70px; height: 70px;
    border-radius: 50%;
    background: radial-gradient(circle at 40% 35%, #e9d27a, var(--gold) 60%, #8d6c1c);
  }
  .back-name {
    position: absolute;
    top: 150px; left: 0; right: 0;
    font-family: "Cormorant Garamond", Georgia, serif;
    font-size: 26px;
    letter-spacing: 9px;
    text-transform: uppercase;
  }
  .back-name-zh {
    position: absolute;
    top: 186px; left: 0; right: 0;
    font-family: "Noto Serif TC", serif;
    font-size: 20px;
    letter-spacing: 2px;
  }
  .back-rule {
    position: absolute;
    top: 222px; left: 120px; right: 120px;
    height: 1px;
    background: var(--back-text);
    opacity: .6;
  }
  .back-tagline {
    position: absolute;
    top: 236px; left: 0; right: 0;
    font-size: 15px;
    font-weight: 300;
    letter-spacing: 3px;
  }

  /* ---------- Front side ---------- */
  .card-front {
    left: 620px;
    background: linear-gradient(180deg, var(--paper) 0%, var(--paper) 55%, var(--paper-shade) 100%);
  }
  .front-band {
    position: absolute;
    left: 0; top: 0;
    width: 540px; height: 324px;
  }
  .front-brand {
    position: absolute;
    right: 30px; top: 36px;
    display: flex; align-items: center; gap: 10px;
  }
  .front-brand-dot {
    width: 44px; height: 44px;
    border-radius: 50%;
    background: radial-gradient(circle at 40% 35%, #e9d27a, var(--gold) 60%, #8d6c1c);
  }
  .front-brand-name {
    font-size: 16px;
    color: var(--navy);
  }
  .person {
    position: absolute;
    left: 30px; top: 64px;
    color: var(--ink);
  }
  .person-name { font-size: 19px; font-weight: 400; }
  .zh { font-family: "Noto Sans TC", sans-serif; }
  .person-name-zh { font-size: 16px; margin-top: 2px; }
  .person-role { font-size: 13px; margin-top: 12px; }
  .person-role-zh { font-size: 13px; margin-top: 2px; }
  .contact {
    position: absolute;
    left: 30px; top: 198px;
    display: grid;
    grid-template-columns: 62px auto;
    row-gap: 3px;
    font-size: 15px;
  }
  .contact dt { color: var(--label); font-weight: 300; }
  .contact dd { color: var(--ink); }
</style>
</head>
<body>

  <section class="card card-back" aria-label="Business card back">
    <div class="back-mark"></div>
    <div class="back-name">Larch Vantage</div>
    <div class="back-name-zh">遠信行</div>
    <div class="back-rule"></div>
    <div class="back-tagline">Trust In The Deal</div>
  </section>

  <section class="card card-front" aria-label="Business card front">
    <svg class="front-band" viewBox="0 0 540 324" aria-hidden="true">
      <defs>
        <linearGradient id="bandFill" x1="0" y1="0" x2="1" y2="0">
          <stop offset="0" stop-color="#0d1c35"/>
          <stop offset=".5" stop-color="#2c5288"/>
          <stop offset="1" stop-color="#0d1c35"/>
        </linearGradient>
      </defs>
      <path d="M0 186 Q200 176 420 160" stroke="#c9ccd1" stroke-width="1" fill="none"/>
      <path d="M0 296 Q270 290 540 270 L540 324 L0 324 Z" fill="url(#bandFill)"/>
    </svg>

    <div class="front-brand">
      <span class="front-brand-dot"></span>
      <span class="front-brand-name">Larch Vantage</span>
    </div>

    <div class="person">
      <div class="person-name">Morris Pelham Ashdown</div>
      <div class="person-name-zh zh">林志遠</div>
      <div class="person-role">Director</div>
      <div class="person-role-zh zh">董事</div>
    </div>

    <dl class="contact">
      <dt>Mobile</dt><dd>0412 555 019</dd>
      <dt>Email</dt><dd>info@larchvantage.com</dd>
      <dt>Web</dt><dd>www.larchvantage.com</dd>
    </dl>
  </section>

</body>
</html>
```